依頼概要
■ 依頼の目的/概要

オゾニドを配合したアイクリームのパッケージ(化粧箱)のデザイン(ラベルシール)を依頼させていただきます。

■ 商品情報

・商品名

K7リフト アイクリーム

ケーセブン リフト アイクリーム

英語表記 :K7 lift eye cream

■対象

30代後半~70代までの女性及び美容(目じりのしわなど)に気を使う男性

■ パッケージの情報

ラベルデザイン面積(エアレス容器を入れる化粧箱) 縦118mm×横40mm 2色

添付資料に商品パッケージ写真がありますので参照お願い致します。

※ロゴの部分は容器でも使用したいと考えています。

■ デザインに希望すること(雰囲気・色・イメージなど)

添付した画像の化粧箱の色は、落ち着いた小豆色ですが、
少々「和」っぽくなってしまいますので、白色の箱も考えています。

O3とはオゾンの事ですので、理化学的なイメージのロゴマークを使ったデザインでお願いします。また、“プラス”の表記は、「+」でも大丈夫です。

■ 納品ファイルの希望

イラストレーター形式(Ver.CS)

■ 利用用途

製品パッケージ及び容器/ウェブサイト/パンフレット等

■ その他/注意点

選択させて頂いたロゴの著作権(財産権)等の扱いはQuindle利用規約に従い、弊社に譲渡をお願いします。フォントや画像素材などを利用する場合は上記利用用途に使用できることを確認し、第三者の知的財産権等に注意して下さい。

以上となります。
どうぞよろしくお願いいたします。
クインドラーの皆様

ご提案どうもありがとうございます。
早い時期にご提案いただけた事で、締め切り前に
私どものイメージを固めることができそうで
とても嬉しく思っております。

これからご提案いただくクインドラー様への希望ですが

使用する容器は、容量30mLと小さく細い容器ですので
デザインの中にグラデーションやエンボスは難しいかなと思います。
気に入ったデザイを何点か選ばせていただきましたが
こちらは、グラデーションやエンボス加工が気に入ったのではなく
小さな容器にでも生えるデザインだと思ったからです。

皆様の力作を心よりお待ち申し上げております。
それでは、どうぞよろしくお願い申し上げます。
Quindlerの皆様

この度は、たくさんのご提案ありがとうございました。
イメージに合うデザインが多く、これから、社内で検討をさせていただきたいと思います。
クインドラーの皆様へ

年末年始が重なった事もあり、連絡の遅れなど、当選のクインドラー様にはご迷惑をおかけしてしまいました。

今回選ばせてさせていただいた理由は、商品を販売するクライアン様が、化学構造で使われる亀の子を丸くアレンジしたデザインをとても気に入られた事が1番の要因です。

他にも良いデザインが何点もあり、採択できなかった事はとても残念でした。

こちらのサイトは、とても良いデザインが集まりますので、今後も新商品のラベルなど
のデザインをご依頼させていただきたいと思っておりますので、今後ともどうぞよろしくお願いたします。
年末のお忙しい中、多くのクインドラー様にご提案頂きどうもありがとうございました。
■ 選んだ理由

先ほど追記させていただいた内容が、選んだ理由となります。

■ 提案者全員のお礼・コメント

どうもありがとうございました。

```html
<!DOCTYPE html>
<html lang="ja">
<head>
<meta charset="utf-8">
<title>K7 lift eye cream — label proposals</title>
<link rel="stylesheet" href="https://fonts.googleapis.com/css2?family=Quicksand:wght@300;400&display=swap">
<style>
  :root {
    --sheet: #ffffff;
    --panel-dark: #2f2321;
    --panel-light: #ffffff;
    --panel-edge: #c8c8c8;
    --ink-ice: #8fd3e3;
    --ink-grey: #9b9b9b;
    --ink-teal: #2f6f67;
  }
  html, body {
    margin: 0;
    width: 849px;
    height: 1200px;
    overflow: hidden;
    background: var(--sheet);
  }
  .sheet {
    position: relative;
    width: 849px;
    height: 1200px;
    font-family: "Quicksand", sans-serif;
  }
  .label {
    position: absolute;
    top: 57px;
    width: 334px;
    height: 990px;
    box-sizing: border-box;
  }
  .label--dark { left: 85px; background: var(--panel-dark); }
  .label--light { left: 453px; background: var(--panel-light); border: 1.5px solid var(--panel-edge); }
  .label svg { display: block; width: 100%; height: 100%; }

  .brand-name { font-weight: 300; font-size: 92px; }
  .product-name { font-weight: 400; font-size: 50px; }
  .product-type { font-weight: 400; font-size: 17px; letter-spacing: 2px; }
  .brand-dot { fill: none; stroke-width: 2.5; }

  .label--dark .ink { fill: var(--ink-ice); }
  .label--dark .brand-dot { stroke: var(--ink-ice); }
  .label--light .ink { fill: var(--ink-grey); }
  .label--light .brand-dot { stroke: var(--ink-grey); }
  .label--light .product-name { fill: var(--ink-teal); }

  .structure-diagram {
    position: absolute;
    left: 356px;
    top: 1090px;
    width: 124px;
    height: 68px;
    background: linear-gradient(#f2f2f2, #e6e6e6);
    border-radius: 6px;
  }
</style>
</head>
<body>
<main class="sheet">
  <section class="label label--dark" aria-label="Dark label proposal">
    <svg viewBox="0 0 334 990">
      <text class="brand-name ink" transform="translate(12 70) rotate(90)" textLength="860" lengthAdjust="spacing">ELARA</text>
      <circle class="brand-dot" cx="260" cy="311" r="25"/>
      <text class="product-name ink" x="312" y="890" text-anchor="end">K7 lift</text>
      <text class="product-type ink" x="312" y="945" text-anchor="end">EYE-CREAM</text>
    </svg>
  </section>

  <section class="label label--light" aria-label="White label proposal">
    <svg viewBox="0 0 334 990">
      <text class="brand-name ink" transform="translate(12 70) rotate(90)" textLength="860" lengthAdjust="spacing">ELARA</text>
      <circle class="brand-dot" cx="260" cy="311" r="25"/>
      <text class="product-name ink" x="312" y="890" text-anchor="end">K7 lift</text>
      <text class="product-type ink" x="312" y="945" text-anchor="end">EYE-CREAM</text>
    </svg>
  </section>

  <div class="structure-diagram" role="img" aria-label="Small molecule structure diagram with annotations"></div>
</main>
</body>
</html>
```